Lanternfield Drinks business cards

We need a business card design for our new logo. The company is modern, progressive, professional, yet approachable. The key products are ready to drink bottles and cans of coffee based beverages.
These cards will be a critical part of the first impression made by our sales organization, business development team, and all external facing personnel.
Card can be a vertical or horizontal orientation.

Target Market(s)

Customers, suppliers, business partners

Industry/Entity Type

Business

Contact Information for Business Card

Business cards should feature Company Name and Logo.

Font styles to use
Serif

Colors

Designer to choose colors to be used in the design.

Requirements
Must have
• Strong readability of Name, phone #, mobile number and email address.
• Job title, website url, Street Address, and other details can be secondary level readability.
Nice to have
• High impact, simplistic quality design.
• Ok to utilize the 'H in the box' separate from the company name

```html
<!DOCTYPE html>
<html lang="en">
<head>
<meta charset="utf-8">
<title>Lanternfield Drinks — Business Cards</title>
<link href="https://fonts.googleapis.com/css2?family=Crimson+Text:wght@400;600;700&display=swap" rel="stylesheet">
<style>
  :root {
    --backdrop: #b9b9b9;
    --orange-light: #e3862f;
    --orange-deep: #c44a27;
    --brand-red: #cf4a25;
    --swoosh-gold: #e08a2c;
    --card-white: #f7f7f7;
    --card-grey: #e6e6e6;
    --ink: #222222;
    --white: #ffffff;
  }
  * { margin: 0; padding: 0; box-sizing: border-box; }
  html, body { width: 1200px; height: 576px; overflow: hidden; }
  body {
    background: var(--backdrop);
    position: relative;
    font-family: "Crimson Text", Georgia, serif;
  }
  .card {
    position: absolute;
    top: 139px;
    width: 484px;
    height: 293px;
    border-radius: 14px;
    overflow: hidden;
    box-shadow: 0 4px 8px rgba(0,0,0,0.25);
  }
  /* Front */
  .card-front {
    left: 82px;
    background: linear-gradient(180deg, var(--orange-light) 0%, #db7530 50%, var(--orange-deep) 100%);
  }
  .front-panel {
    position: absolute;
    top: 0;
    width: 110px;
    height: 100%;
    background: rgba(255,255,255,0.06);
    border-radius: 0 0 14px 14px;
  }
  .front-mark {
    position: absolute;
    left: 50%;
    top: 78px;
    width: 76px;
    height: 76px;
    margin-left: -38px;
    border: 4px solid var(--white);
  }
  .front-name {
    position: absolute;
    left: 0;
    right: 0;
    top: 168px;
    text-align: center;
    color: var(--white);
    font-weight: 700;
    font-size: 34px;
    letter-spacing: 1px;
    text-transform: uppercase;
    line-height: 1;
  }
  /* Back */
  .card-back {
    left: 602px;
    background: linear-gradient(180deg, var(--card-white) 0%, var(--card-grey) 100%);
    color: var(--ink);
  }
  .back-panel {
    position: absolute;
    top: 6px;
    height: 240px;
    width: 170px;
    background: rgba(0,0,0,0.025);
    border-radius: 16px;
  }
  .back-mark {
    position: absolute;
    left: 102px;
    top: 38px;
    width: 64px;
    height: 64px;
    border: 4px solid var(--brand-red);
  }
  .back-name {
    position: absolute;
    left: 20px;
    width: 228px;
    top: 112px;
    text-align: center;
    color: var(--brand-red);
    font-weight: 700;
    font-size: 26px;
    line-height: 1.05;
    text-transform: uppercase;
  }
  .person {
    position: absolute;
    right: 28px;
    top: 34px;
    text-align: right;
  }
  .person-name { color: var(--brand-red); font-weight: 700; font-size: 19px; line-height: 1.1; }
  .person-title { font-size: 12px; margin-top: 2px; }
  .contact {
    position: absolute;
    right: 22px;
    top: 119px;
    list-style: none;
    text-align: right;
    font-size: 13px;
    line-height: 16px;
  }
  .contact li { display: flex; justify-content: flex-end; align-items: center; gap: 6px; }
  .contact .icon { width: 10px; height: 10px; fill: var(--brand-red); }
  .address {
    position: absolute;
    right: 38px;
    top: 180px;
    text-align: right;
    font-size: 13px;
    line-height: 16px;
  }
  .wave { position: absolute; left: 0; bottom: 0; width: 484px; height: 70px; }
  .website {
    position: absolute;
    right: 28px;
    bottom: 17px;
    color: var(--white);
    font-size: 12px;
  }
</style>
</head>
<body>
  <section class="card card-front" aria-label="Card front">
    <div class="front-panel" style="left:90px"></div>
    <div class="front-panel" style="left:300px"></div>
    <div class="front-mark"></div>
    <div class="front-name">Lanternfield Drinks</div>
  </section>

  <section class="card card-back" aria-label="Card back">
    <div class="back-panel" style="left:60px"></div>
    <div class="back-panel" style="left:274px"></div>
    <div class="back-mark"></div>
    <div class="back-name">Lanternfield Drinks</div>

    <div class="person">
      <div class="person-name">John Doe Smith</div>
      <div class="person-title">Managing Director</div>
    </div>

    <ul class="contact">
      <li>555.555.5555
        <svg class="icon" viewBox="0 0 10 10"><path d="M1 3 Q5 0 9 3 L8 4.5 L6.5 3.8 L6.5 3 Q5 2.6 3.5 3 L3.5 3.8 L2 4.5 Z M2.5 5 H7.5 L8.5 9 H1.5 Z"/></svg>
      </li>
      <li>666.666.7777
        <svg class="icon" viewBox="0 0 10 10"><path d="M2.5 0.5 H7.5 V9.5 H2.5 Z M3.5 1.5 V7 H6.5 V1.5 Z"/></svg>
      </li>
      <li>johndoe@yourwebsite.com
        <svg class="icon" viewBox="0 0 10 10"><path d="M0.5 2 H9.5 V8 H0.5 Z M1 2.5 L5 5.5 L9 2.5" stroke="#fff" stroke-width="0.8"/></svg>
      </li>
    </ul>

    <div class="address">234 Anywhere St.,<br>Any Town, US 123456</div>

    <svg class="wave" viewBox="0 0 484 70" preserveAspectRatio="none" aria-hidden="true">
      <path d="M0 25 C80 60 160 68 260 42 C340 22 420 20 484 30 L484 70 L0 70 Z" fill="var(--orange-deep)"/>
      <path d="M0 4 C70 40 150 58 250 36 C340 16 420 10 484 20 L484 27 C420 18 340 26 255 44 C150 66 70 50 0 16 Z" fill="var(--swoosh-gold)"/>
      <path d="M0 16 C70 50 150 66 255 44 C340 26 420 18 484 27 L484 31 C420 22 340 30 258 48 C150 72 70 58 0 24 Z" fill="#ffffff"/>
    </svg>
    <div class="website">www.yourwebsite.com</div>
  </section>
</body>
</html>
```